Hypnotherapy- past life regression-life between lives therapist needs a website

I need a website that is enticing and spiritual in its feeling. It needs to have a lot of beautiful nature pictures included. The theme is "Willowmere Hollow- what could you uncover....Tides Lanterns Compass"
Because all of us have the answers to living our best life, they are in our subconcious. But not everyone is capable of accessing them. Hypnosis accesses the subconcious and helps to create new neural pathways in the brain which can create new behaviors and responses to situations.
Hypnosis can help with anxiety, pain relief, weight loss, smoking/vaping cessation, self confidence......anything about yourself that you want to change.
Exploration of past lives and life between lives can reveal things related to ones current life. For example, perhaps your fear of deep water is a result of drowning in a past life. Once this has been discovered, it can lead to changes in ones current life.
Almost any personal behavior one wants to change, can be helped through hypnotherapy.
I need a page for testimonials, a place for scheduling (I will have a link to my scheduling app) some information about hypnotherapy.
I am uploading my logo files. My business card will be using the black and gold style, but my website does not have to reflect that. It can be based on the caramel and deep green like full color logo. Earthy, calm colors.
I also like the mock up of my logo on the beach and there was one on a starry night sky that I also liked.
Target Market(s)
men and women ages 25-50
Industry/Entity Type
natural health and wellness, spirituality
Number of Pages Required
4 page
Requirements
Must have
- a page for testimonials, perhaps with a beautiful nature picture with each one, I will have approximately 6. A link to schedule a complimentary intro session, preferably on the first page
Should not have
- no swinging watches or other sterotyped hypnosis symbols

```html
<!DOCTYPE html>
<html lang="en">
<head>
<meta charset="utf-8">
<title>Willowmere Hollow – Hypnotherapy</title>
<link href="https://fonts.googleapis.com/css2?family=Merriweather:wght@400;700&family=Inter:wght@400;500;600;700&display=swap" rel="stylesheet">
<style>
:root{
  --caramel:#e0852a;
  --caramel-dark:#c96f1c;
  --moss:#5e6237;
  --moss-dark:#4c5029;
  --ink:#14213d;
  --text:#333;
  --muted:#6b6b6b;
  --panel:#f3f3f3;
  --white:#fff;
}
*{box-sizing:border-box;margin:0;padding:0}
html,body{width:1200px;height:4814px;overflow:hidden}
body{position:relative;font-family:"Inter",Arial,sans-serif;color:var(--text);background:var(--white)}
.abs{position:absolute}
.serif{font-family:"Merriweather",Georgia,serif}
.btn{position:absolute;display:flex;align-items:center;justify-content:center;border-radius:30px;color:var(--white);font-size:13px;font-weight:500;letter-spacing:.3px;text-transform:uppercase}
.btn--caramel{background:var(--caramel)}
.btn--moss{background:var(--moss)}

/* hero */
.hero{position:absolute;left:0;top:0;width:1200px;height:766px;overflow:hidden}
.hero__photo{position:absolute;inset:0;background:linear-gradient(180deg,#e9eeea 0%,#b9c9bf 18%,#6f8f7a 40%,#8fb2bd 58%,#4f6c55 78%,#2f4a2c 100%)}
.hero__veil{position:absolute;inset:0;background:linear-gradient(180deg,rgba(255,255,255,.55) 0%,rgba(255,255,255,.05) 30%,rgba(0,0,0,0) 100%)}
.brand{position:absolute;left:104px;top:40px;display:flex;align-items:center;gap:10px}
.brand__dot{width:26px;height:26px;border-radius:50%;background:var(--caramel)}
.brand__name{font-family:"Merriweather",Georgia,serif;font-weight:700;font-size:17px;color:var(--caramel);line-height:1.2;width:110px}
.nav{position:absolute;left:396px;top:66px;display:flex;gap:0;font-size:13px;color:#222}
.nav a{text-decoration:none;color:inherit;margin-right:28px}
.hero__title{position:absolute;left:0;width:1200px;top:282px;text-align:center;font-family:"Merriweather",Georgia,serif;font-weight:700;font-size:66px;color:var(--white);letter-spacing:1px}
.hero__sub{position:absolute;left:290px;width:620px;top:366px;text-align:center;font-size:17px;line-height:1.4;color:var(--white)}
.hero__wave{position:absolute;left:0;top:660px}

/* about */
.about__title{left:151px;top:895px;font-size:28px;color:var(--moss)}
.about__text{left:151px;top:956px;width:400px;font-size:11.5px;line-height:1.45;color:#222}
.about__text p+p{margin-top:14px}

/* solutions */
.solutions{position:absolute;left:0;top:1320px;width:1200px;height:790px;overflow:hidden}
.solutions__sea{position:absolute;left:0;top:480px;width:1200px;height:310px;background:linear-gradient(180deg,rgba(224,133,42,0) 0%,#e8893a 25%,#d9612a 45%,#7a3a1e 70%,#3a2018 100%)}
.solutions__title{position:absolute;left:0;width:1200px;top:138px;text-align:center;font-size:26px;color:var(--white)}
.card{position:absolute;top:235px;width:232px;height:204px;background:var(--white)}
.card__img{width:100%;height:153px}
.card__label{text-align:center;font-family:"Merriweather",Georgia,serif;font-weight:700;font-size:16px;color:#222;padding-top:16px}

/* testimonial */
.testi__title{left:114px;top:2248px;font-size:40px;font-weight:700;color:var(--ink)}
.testi__intro{left:114px;top:2316px;width:520px;font-size:15.5px;line-height:1.5;color:var(--muted)}
.quote{position:absolute;left:114px;top:2426px;width:540px;height:224px;background:#ececec;border-radius:10px;padding:30px 34px}
.quote__mark{font-family:"Merriweather",Georgia,serif;font-weight:700;font-size:48px;color:#3b9a3b;line-height:.7;height:40px}
.quote__text{font-size:20px;line-height:1.4;color:#222}
.quote__tail{position:absolute;left:30px;bottom:-14px;width:0;height:0;border-left:12px solid transparent;border-right:12px solid transparent;border-top:14px solid #ececec}
.author__avatar{left:114px;top:2692px;width:60px;height:60px;border-radius:4px;background:linear-gradient(135deg,#c9b6a6,#6b5548)}
.author__name{left:194px;top:2700px;font-size:15px;font-weight:600;color:#111}
.author__role{left:194px;top:2727px;font-size:13px;color:#666}
.author__role b{color:#2e7d32}
.arrow{position:absolute;top:2699px;width:46px;height:46px;border-radius:50%;border:2px solid var(--caramel);display:flex;align-items:center;justify-content:center}
.arrow--fill{background:var(--caramel)}
.testi__photo{left:677px;top:2258px;width:446px;height:540px;border-radius:10px;background:linear-gradient(180deg,#f0f0ee 0%,#e6e3de 60%,#d9d3cb 100%)}

/* blog */
.blog{position:absolute;left:0;top:2880px;width:1200px;height:710px}
.blog__title{position:absolute;left:0;width:1160px;top:95px;text-align:center;font-size:25px;font-weight:600;color:var(--white)}
.post{position:absolute;top:170px;width:309px;height:469px;background:var(--white)}
.post__img{height:219px}
.post__body{padding:30px 26px 0}
.post__meta{font-size:10.5px;color:#999}
.post__title{font-size:15px;font-weight:500;color:#111;line-height:1.45;margin-top:12px}
.post__excerpt{font-size:11.5px;color:#888;line-height:1.6;margin-top:10px}
.post__more{display:inline-flex;align-items:center;gap:10px;margin-top:22px;border:1px solid #cfd8ef;padding:9px 18px;font-size:10px;font-weight:600;color:#3358c4}

/* contact */
.learn__title{left:117px;top:3716px;width:360px;font-size:27px;font-weight:600;line-height:1.22;color:#111}
.learn__text{left:117px;top:3824px;width:300px;font-size:12.5px;line-height:1.65;color:#222}
.info{position:absolute;left:117px;display:flex;align-items:center;gap:14px;font-size:11.5px;color:#111;line-height:1.4}
.info__icon{width:54px;height:54px;border-radius:50%;background:var(--caramel);border:2px solid var(--moss);display:flex;align-items:center;justify-content:center}
.form{position:absolute;left:505px;top:3691px;width:648px;height:537px;background:var(--panel);border-radius:30px}
.form__title{position:absolute;left:42px;top:88px;font-size:27px;font-weight:600;color:#111}
.field{position:absolute;height:48px;border:1.5px solid #7d84ad;font-size:13px;color:#333;padding:14px 22px}
.submit{position:absolute;left:43px;top:447px;width:160px;height:49px;border-radius:30px;background:var(--moss);color:var(--white);font-size:13px;font-weight:600;display:flex;align-items:center;justify-content:center}

/* footer */
.footer{position:absolute;left:0;top:4282px;width:1200px;height:532px;background:radial-gradient(ellipse at 50% 30%,#6a5aa6 0%,#3e3878 35%,#1e1f4a 70%,#14163a 100%)}
.footer__glow{position:absolute;left:0;bottom:0;width:1200px;height:160px;background:linear-gradient(180deg,rgba(0,0,0,0),rgba(180,140,190,.35) 60%,rgba(20,20,40,.9))}
.footer__brand{position:absolute;left:0;width:1200px;top:216px;display:flex;justify-content:center;align-items:center;gap:14px}
.footer__brand span{font-family:"Merriweather",Georgia,serif;font-weight:700;font-size:30px;color:var(--white);letter-spacing:1px}
.footer__ring{width:30px;height:30px;border-radius:50%;border:2px solid var(--white)}
.footer__nav{position:absolute;left:0;width:1200px;top:346px;display:flex;justify-content:center;gap:0;font-size:16px;color:var(--white)}
.footer__nav span{margin:0 14px}
</style>
</head>
<body>

<header class="hero">
  <div class="hero__photo" role="img" aria-label="Misty forested valley with a winding lake"></div>
  <div class="hero__veil"></div>
  <div class="brand"><div class="brand__dot"></div><div class="brand__name">Willowmere Hollow</div></div>
  <nav class="nav"><a>Home</a><a>Hypnosis Solutions</a><a>About Us</a><a>Testimonials</a><a>Blog</a><a>Contact</a></nav>
  <div class="btn btn--caramel" style="left:914px;top:60px;width:172px;height:36px">Make Appointment</div>
  <h1 class="hero__title">Don't Suffer in silence</h1>
  <p class="hero__sub">Let Hypnotherapy help you get to the root of your issues and make positive changes to your life</p>
  <div class="btn btn--moss" style="left:514px;top:434px;width:170px;height:34px;font-size:12px">Make Appointment</div>
  <svg class="hero__wave" width="1200" height="106" viewBox="0 0 1200 106">
    <path d="M0 62 C300 -10 800 -15 1200 58 L1200 106 L0 106Z" fill="var(--moss)"/>
    <path d="M0 106 L0 92 C320 30 820 28 1200 102 L1200 106Z" fill="#fff"/>
  </svg>
</header>

<section class="about">
  <h2 class="abs serif about__title">Who We Are</h2>
  <div class="abs about__text">
    <p>Lorem ipsum dolor sit amet consectetur. Volutpat turpis quam euismod ac est. Lacinia ac cursus sodales donec aliquam accumsan. A blandit vitae nunc aliquet tempor platea lectus. Pretium aliquam auctor nisl bibendum pretium imperdiet. Sed tristique et auctor nisl enim. Nisl adipiscing vulputate volutpat facilisi dignissim tristique lectus.</p>
    <p>Nisl amet tellus eget etiam eget. Justo non diam cursus lobortis condimentum. Malesuada at.</p>
  </div>
  <div class="btn btn--caramel" style="left:146px;top:1134px;width:172px;height:36px;font-size:12px">Read More</div>
  <svg class="abs" style="left:640px;top:800px" width="460" height="450" viewBox="0 0 460 450">
    <defs>
      <radialGradient id="shore" cx="40%" cy="35%" r="75%">
        <stop offset="0" stop-color="#5fcfd6"/><stop offset=".55" stop-color="#9fe0e0"/><stop offset=".8" stop-color="#efe4d4"/><stop offset="1" stop-color="#e6d6c2"/>
      </radialGradient>
    </defs>
    <circle cx="222" cy="218" r="212" fill="var(--caramel)"/>
    <circle cx="240" cy="230" r="212" fill="var(--moss)"/>
    <circle cx="238" cy="220" r="198" fill="#fff"/>
    <circle cx="238" cy="220" r="192" fill="url(#shore)" role="img" aria-label="Aerial view of turquoise waves meeting a sandy beach"/>
  </svg>
</section>

<section class="solutions">
  <svg class="abs" style="left:0;top:0" width="1200" height="790" viewBox="0 0 1200 790">
    <path d="M0 78 C300 -10 800 -10 1200 50 L1200 790 L0 790Z" fill="var(--moss)"/>
    <path d="M0 110 C360 0 820 -5 1200 92 L1200 790 L0 790Z" fill="var(--caramel)"/>
  </svg>
  <div class="solutions__sea" role="img" aria-label="Sunset over ocean waves"></div>
  <h2 class="serif solutions__title">Hypnotherapy Solutions</h2>
  <div class="card" style="left:114px"><div class="card__img" style="background:linear-gradient(160deg,#777,#3a3a3a)" role="img" aria-label="Hands breaking a cigarette"></div><div class="card__label">Addiction</div></div>
  <div class="card" style="left:361px"><div class="card__img" style="background:linear-gradient(160deg,#4a4a4a,#1a1a1a)" role="img" aria-label="Person sitting alone in a dark room"></div><div class="card__label" style="padding-top:20px">Anxiety</div></div>
  <div class="card" style="left:609px"><div class="card__img" style="background:radial-gradient(circle at 45% 50%,#b8806a,#3c2a2c 60%,#1c1c26)" role="img" aria-label="Abstract head dissolving into fragments"></div><div class="card__label" style="padding-top:18px">Overcoming Trauma</div></div>
  <div class="card" style="left:856px"><div class="card__img" style="background:linear-gradient(160deg,#f6e4e0,#e8c8c4)" role="img" aria-label="Magnifying glass over a medical cross"></div><div class="card__label">Health</div></div>
  <div class="btn btn--moss" style="left:469px;top:474px;width:260px;height:36px;font-size:12px">Book Your Free Consultation</div>
</section>

<section class="testimonial">
  <h2 class="abs testi__title">Client Testimonial</h2>
  <p class="abs testi__intro">Praesent interdum eu magna a imperdiet. Ut orci ipsum, rutrum id tortor sit amet, mattis cursus libero. Phasellus facilisis malesuada nibh vel commodo.</p>
  <div class="quote">
    <div class="quote__mark">”</div>
    <p class="quote__text">Lorem ipsum dolor sit amet consectetur. In in consectetur orci tortor urna. A odio nibh et nunc risus. Quam praesent accumsan hac quis aliquet mollis praesent risus vulputate. Eu tempor laoreet.</p>
    <div class="quote__tail"></div>
  </div>
  <div class="abs author__avatar" role="img" aria-label="Client portrait"></div>
  <div class="abs author__name">Dorian Fairclough</div>
  <div class="abs author__role">Founder of <b>Mossline</b></div>
  <div class="arrow" style="left:550px"><svg width="18" height="14" viewBox="0 0 18 14"><path d="M17 7H2M7 1L1 7l6 6" fill="none" stroke="#333" stroke-width="1.6"/></svg></div>
  <div class="arrow arrow--fill" style="left:608px"><svg width="18" height="14" viewBox="0 0 18 14"><path d="M1 7h15M11 1l6 6-6 6" fill="none" stroke="#222" stroke-width="1.6"/></svg></div>
  <div class="abs testi__photo" role="img" aria-label="Smiling client portrait on a light background"></div>
</section>

<section class="blog">
  <svg class="abs" style="left:0;top:0" width="1200" height="710" viewBox="0 0 1200 710">
    <path d="M0 100 C360 20 820 -10 1200 45 L1200 710 L0 710Z" fill="var(--caramel)"/>
    <path d="M0 118 C360 40 820 20 1200 70 L1200 705 L0 705Z" fill="var(--moss)"/>
  </svg>
  <h2 class="blog__title">Latest Blog</h2>
  <article class="post" style="left:112px">
    <div class="post__img" style="background:radial-gradient(circle at 50% 50%,#e0a060,#6b3a22 45%,#1e1a1c)" role="img" aria-label="Swirling abstract light"></div>
    <div class="post__body"><div class="post__meta">22 Oct, 2020 &nbsp;/&nbsp; 246 Comments</div><h3 class="post__title">Duis magna risus, convallis vel purus eu, sollicitudin volutpat velit.</h3><p class="post__excerpt">Maecenas blandit auctor tempor. Class aptent taciti sociosqu ad litora torquent per conubia nostra.</p><span class="post__more">READ MORE <svg width="14" height="10" viewBox="0 0 14 10"><path d="M0 5h12M8 1l4 4-4 4" fill="none" stroke="#3358c4" stroke-width="1.4"/></svg></span></div>
  </article>
  <article class="post" style="left:445px">
    <div class="post__img" style="background:linear-gradient(180deg,#c9dce6,#e9eef0 55%,#b9c6b8)" role="img" aria-label="Woman resting by a calm lake"></div>
    <div class="post__body"><div class="post__meta">8 Sep, 2020 &nbsp;/&nbsp; 246 Comments</div><h3 class="post__title">Donec ut ex eu libero euismod dapibus id quis ipsum.</h3><p class="post__excerpt">Phasellus non feugiat turpis, non gravida lorem. Nulla fermentum odio in dolor dapibus, ac eleifend lectus ullamcorper.</p><span class="post__more">READ MORE <svg width="14" height="10" viewBox="0 0 14 10"><path d="M0 5h12M8 1l4 4-4 4" fill="none" stroke="#3358c4" stroke-width="1.4"/></svg></span></div>
  </article>
  <article class="post" style="left:778px">
    <div class="post__img" style="background:linear-gradient(180deg,#d9c6c8,#e7d9d6 50%,#9a948e)" role="img" aria-label="Lifeguard hut on a quiet beach"></div>
    <div class="post__body"><div class="post__meta">24 May, 2020 &nbsp;/&nbsp; 246 Comments</div><h3 class="post__title">Maecenas congue cursus metus eget bibendum phasellus dign.</h3><p class="post__excerpt">Praesent semper enim at lacus sagittis, non semper eros ullamcorper. Duis id elemtum nisl, eu tincidunt nisl.</p><span class="post__more">READ MORE <svg width="14" height="10" viewBox="0 0 14 10"><path d="M0 5h12M8 1l4 4-4 4" fill="none" stroke="#3358c4" stroke-width="1.4"/></svg></span></div>
  </article>
</section>

<section class="contact">
  <h2 class="abs learn__title">Learn More About This Innovative New Treatment Option</h2>
  <p class="abs learn__text">Lorem ipsum dolor sit amet consectetur. Odio elementum lectus mattis ac nunc sed. Pharetra risus neque proin enim duis felis cras sit tortor. Est commodo sed sed fusce. Vulputate nunc commodo auctor amet neque quisque pretium sed nulla. Ligula sit elit justo rutrum tincidunt.</p>
  <div class="info" style="top:3978px"><div class="info__icon"><svg width="20" height="16" viewBox="0 0 20 16"><rect x="1" y="1" width="18" height="14" rx="2" fill="none" stroke="#fff" stroke-width="1.5"/><path d="M1 2l9 7 9-7" fill="none" stroke="#fff" stroke-width="1.5"/></svg></div><div>Email<br>hello@willowmerehollow.com</div></div>
  <div class="info" style="top:4055px"><div class="info__icon"><svg width="20" height="20" viewBox="0 0 24 24"><path d="M5 3h4l2 5-3 2a11 11 0 006 6l2-3 5 2v4a2 2 0 01-2 2A17 17 0 013 5a2 2 0 012-2z" fill="none" stroke="#fff" stroke-width="1.5"/></svg></div><div>Call Us<br>(00) 418 207 936</div></div>
  <div class="info" style="top:4133px"><div class="info__icon"><svg width="20" height="20" viewBox="0 0 20 20"><circle cx="10" cy="10" r="8.5" fill="none" stroke="#fff" stroke-width="1.5"/><path d="M10 5v5l3 2" fill="none" stroke="#fff" stroke-width="1.5"/></svg></div><div>Mon - Sat 9.00 - 18.00<br>Sunday Closed</div></div>

  <div class="form">
    <h2 class="form__title">Get in Touch</h2>
    <div class="field" style="left:42px;top:142px;width:264px">First name*</div>
    <div class="field" style="left:339px;top:142px;width:264px">Last name*</div>
    <div class="field" style="left:42px;top:217px;width:272px">Phone Number*</div>
    <div class="field" style="left:339px;top:217px;width:282px">Email*</div>
    <div class="field" style="left:42px;top:292px;width:578px;height:129px">Your Message</div>
    <div class="submit">Submit Message</div>
  </div>
</section>

<footer class="footer" role="img" aria-label="Starry purple night sky over the horizon">
  <div class="footer__glow"></div>
  <div class="footer__brand"><div class="footer__ring"></div><span>Willowmere Hollow</span></div>
  <nav class="footer__nav"><span>Home</span><span>Hypnosis Solutions</span><span>About Us</span><span>Testimonials</span><span style="margin-left:30px">Blog</span><span style="margin-left:50px">Contact</span></nav>
</footer>

</body>
</html>
```